Truck Drivers Using App w/Jobsite Checklist

Looking for an 8" x 11" flyer that conveys to our customers (roofing contractors) that our drivers have tablets in each truck that have an app with a jobsite checklist that gives contractors less real time notifications and mistakes are caught with photos.
Should read something like this:
Ever wonder if your material has been delivered? We've got a solution for that!
All Trucks are equipped with dash-mounted tablet.
Here's what you get access to:
- Real Time Email Confirmation of Delivery
- Photos of Material Placement
- Before/After Photo of Driveway
- Material List of Products Delivered
- Homeowner Sign Off
Maybe a collage of the different photos available.
Target Market(s)
Roofing/Building Contractors
Industry/Entity Type
Roofing
Requirements
Must have
- website: www.harborfinchdepot.com
- tagline: Building Relationships, Building Trust - a Tradition Since 1905
- Photoshop format for further editing
Nice to have
- A smooth look to it.
- A collage of the photos avail on app

```html
<!DOCTYPE html>
<html lang="en">
<head>
<meta charset="utf-8">
<title>Harbor Finch Depot – Delivery Tablet Flyer</title>
<link href="https://fonts.googleapis.com/css2?family=Roboto+Condensed:wght@400;500;700&family=Open+Sans:wght@600;700&display=swap" rel="stylesheet">
<style>
  :root{
    --brand-blue:#25379a;
    --brand-blue-dark:#1c2a80;
    --ink:#1a1a1a;
    --paper:#ffffff;
    --stage:#e9e9ea;
  }
  *{margin:0;padding:0;box-sizing:border-box}
  html,body{width:801px;height:1200px;overflow:hidden;background:var(--stage)}
  .flyer{position:absolute;left:0;top:83px;width:801px;height:1034px;background:var(--paper);overflow:hidden;font-family:"Roboto Condensed",sans-serif}
  .flyer-art{position:absolute;left:0;top:0;width:801px;height:1034px}
  .eyebrow{position:absolute;left:32px;top:38px;font-size:22px;font-weight:500;color:var(--brand-blue)}
  .headline{position:absolute;left:32px;top:72px;font-size:47px;line-height:48px;font-weight:700;color:var(--ink);text-transform:uppercase}
  .subline{position:absolute;left:32px;top:196px;font-size:21px;line-height:26px;font-weight:500;color:var(--brand-blue)}
  .access-title{position:absolute;left:52px;top:696px;font-size:37px;font-weight:500;color:var(--brand-blue)}
  .access-list{position:absolute;left:52px;top:764px;list-style:none}
  .access-list li{display:flex;align-items:center;height:36.5px;font-size:23px;font-weight:500;color:var(--brand-blue)}
  .access-list svg{width:22px;height:22px;margin-right:14px;flex:none}
  .tagline-badge{position:absolute;left:548px;top:736px;width:260px;height:260px}
  .tagline-badge p{position:absolute;inset:0;display:flex;align-items:center;justify-content:center;text-align:center;font-family:"Open Sans",sans-serif;font-weight:700;font-size:20px;line-height:25px;color:var(--paper);transform:rotate(-8deg)}
  .footer-band{position:absolute;left:0;bottom:0;width:801px;height:46px;background:var(--brand-blue);display:flex;align-items:center;justify-content:center;font-family:"Open Sans",sans-serif;font-weight:700;font-size:21px;color:var(--paper)}
</style>
</head>
<body>
<main class="flyer">
  <svg class="flyer-art" viewBox="0 0 801 1034">
    <defs>
      <linearGradient id="cabGrad" x1="0" y1="0" x2="0" y2="1">
        <stop offset="0" stop-color="#d7dbe0"/>
        <stop offset="0.35" stop-color="#b9bcbf"/>
        <stop offset="0.6" stop-color="#5a5d62"/>
        <stop offset="1" stop-color="#2c2e32"/>
      </linearGradient>
      <linearGradient id="truckGrad" x1="0" y1="0" x2="0" y2="1">
        <stop offset="0" stop-color="#9dc0e6"/><stop offset="0.55" stop-color="#e8ecef"/><stop offset="1" stop-color="#55585c"/>
      </linearGradient>
      <linearGradient id="bundleGrad" x1="0" y1="0" x2="1" y2="1">
        <stop offset="0" stop-color="#7aa0c8"/><stop offset="0.5" stop-color="#e9eef3"/><stop offset="1" stop-color="#a8323a"/>
      </linearGradient>
      <linearGradient id="shingleGrad" x1="0" y1="0" x2="0" y2="1">
        <stop offset="0" stop-color="#c9b99c"/><stop offset="0.5" stop-color="#d8dde2"/><stop offset="1" stop-color="#8a8378"/>
      </linearGradient>
    </defs>

    <rect class="cab-photo" role="img" aria-label="Photo from a truck cab: highway through the windshield with a dash-mounted tablet showing the delivery checklist app" x="0" y="0" width="801" height="700" fill="url(#cabGrad)"/>

    <path class="top-panel" d="M0 0 H600 C590 150 460 260 300 280 C180 300 60 330 0 380 Z" fill="var(--paper)"/>
    <path class="top-panel-edge" d="M300 280 C180 300 60 330 0 380" fill="none" stroke="var(--brand-blue)" stroke-width="5"/>

    <path class="bottom-panel" d="M0 640 C240 560 520 720 801 600 V1034 H0 Z" fill="var(--paper)"/>
    <path d="M0 640 C240 560 520 720 801 600" fill="none" stroke="var(--brand-blue)" stroke-width="6"/>
    <path d="M0 660 C240 585 520 745 801 625" fill="none" stroke="var(--brand-blue)" stroke-width="3"/>

    <g class="photo-collage">
      <circle cx="166" cy="517" r="129" fill="var(--brand-blue)"/>
      <circle role="img" aria-label="Photo of a delivery truck with boom loader carrying material" cx="166" cy="517" r="122" fill="url(#truckGrad)"/>
      <circle cx="455" cy="570" r="106" fill="var(--brand-blue)"/>
      <circle role="img" aria-label="Photo of strapped shingle bundles on the truck bed" cx="455" cy="570" r="99" fill="url(#bundleGrad)"/>
      <circle cx="690" cy="654" r="99" fill="var(--brand-blue)"/>
      <circle role="img" aria-label="Photo of material placed on the roof at the jobsite" cx="690" cy="654" r="92" fill="url(#shingleGrad)"/>
    </g>
  </svg>

  <p class="eyebrow">Ever Wonder If Your Material Has Been Delivered?</p>
  <h1 class="headline">We've Got A Solution<br>For That!</h1>
  <p class="subline">All Trucks are equipped with dash-<br>mounted tablet.</p>

  <h2 class="access-title">What You Get Access To:</h2>
  <ul class="access-list">
    <li><svg viewBox="0 0 22 22"><circle cx="10" cy="12" r="8" fill="none" stroke="currentColor" stroke-width="1.8"/><path d="M6 12 l3 3 l10-11" fill="none" stroke="currentColor" stroke-width="2"/></svg>Real Time Email Confirmation of Delivery</li>
    <li><svg viewBox="0 0 22 22"><circle cx="10" cy="12" r="8" fill="none" stroke="currentColor" stroke-width="1.8"/><path d="M6 12 l3 3 l10-11" fill="none" stroke="currentColor" stroke-width="2"/></svg>Photos of Material Placement</li>
    <li><svg viewBox="0 0 22 22"><circle cx="10" cy="12" r="8" fill="none" stroke="currentColor" stroke-width="1.8"/><path d="M6 12 l3 3 l10-11" fill="none" stroke="currentColor" stroke-width="2"/></svg>Before/After Photo of Driveway</li>
    <li><svg viewBox="0 0 22 22"><circle cx="10" cy="12" r="8" fill="none" stroke="currentColor" stroke-width="1.8"/><path d="M6 12 l3 3 l10-11" fill="none" stroke="currentColor" stroke-width="2"/></svg>Material List of Products Delivered</li>
    <li><svg viewBox="0 0 22 22"><circle cx="10" cy="12" r="8" fill="none" stroke="currentColor" stroke-width="1.8"/><path d="M6 12 l3 3 l10-11" fill="none" stroke="currentColor" stroke-width="2"/></svg>Homeowner Sign Off</li>
  </ul>

  <div class="tagline-badge">
    <svg viewBox="0 0 260 260" width="260" height="260" aria-hidden="true">
      <polygon fill="var(--brand-blue)" points="260,130 234.3,158 242.6,195 206.4,206.4 195,242.6 158,234.3 130,260 102,234.3 65,242.6 53.6,206.4 17.4,195 25.7,158 0,130 25.7,102 17.4,65 53.6,53.6 65,17.4 102,25.7 130,0 158,25.7 195,17.4 206.4,53.6 242.6,65 234.3,102"/>
    </svg>
    <p>Building<br>Relationships,<br>Building<br>Trust - a Tradition<br>Since 1905</p>
  </div>

  <footer class="footer-band">www.harborfinchdepot.com</footer>
</main>
</body>
</html>
```